We want a hot New Design for our IT company Web Site

We have a basic website with some general information and lots of mostly words and generic pictures we want to make it look and feel a lot more modern and slick. The site needs to work on mobile devices as well as desktops.

Target Market(s)

Business customers

Industry/Entity Type

It Company

Coding

Coded - Design and coding required

Number of Pages Required

5+ page

Requirements
Must have
• Sleek new Design making it look and feel more modern and less boring
Nice to have
• If it can have a better flow to it rather then have the std Drop down menus it has now.

```html
<!DOCTYPE html>
<html lang="en">
<head>
<meta charset="utf-8">
<title>Norbridge Solutions Group</title>
<link rel="stylesheet" href="https://fonts.googleapis.com/css2?family=Open+Sans:wght@400;600;700&family=Roboto+Condensed:wght@400;700&display=swap">
<style>
:root{
  --brand:#1a5fb4;
  --ink:#333;
  --muted:#666;
  --line:#d8dde3;
  --page:#eceef1;
  --band:#0b0b0b;
  --footer:#1c56a8;
  --white:#fff;
}
*{box-sizing:border-box;margin:0;padding:0}
html,body{width:867px;height:1200px;overflow:hidden}
body{font-family:"Open Sans",Arial,sans-serif;color:var(--ink);background:var(--page)}
a{color:inherit;text-decoration:none}

.site-header{height:87px;background:var(--white);position:relative}
.brand{position:absolute;left:112px;top:14px;display:flex;align-items:center;gap:8px}
.brand-mark{width:20px;height:20px;background:var(--brand)}
.brand-name{font-family:"Roboto Condensed",Arial,sans-serif;font-weight:700;font-size:21px;color:var(--brand)}
.call{position:absolute;right:112px;top:10px;display:flex;align-items:center;gap:8px}
.call svg{width:20px;height:20px}
.call-text{font-size:10px;color:var(--muted);line-height:1.2}
.call-text strong{display:block;font-size:14px;color:var(--brand);font-weight:700}
.main-nav{position:absolute;right:112px;top:56px;display:flex}
.main-nav a{font-size:11px;padding:6px 10px;color:var(--ink);border-left:1px solid var(--line)}
.main-nav a:first-child{border-left:none}
.main-nav a.is-active{border-bottom:2px solid var(--brand);color:var(--brand);font-weight:600}

.hero{position:relative;height:318px;overflow:hidden}
.hero-photo{position:absolute;inset:0;background:radial-gradient(circle at 30% 45%,#6d8fae 0%,#36597c 35%,#1d3550 70%,#0f1f33 100%)}
.hero-copy{position:absolute;left:400px;top:122px;color:var(--white)}
.hero-copy h1{font-family:"Roboto Condensed",Arial,sans-serif;font-size:28px;font-weight:700}
.hero-copy p{font-size:14px;margin-top:2px}
.hero-arrow{position:absolute;top:147px;width:18px;height:24px;background:rgba(0,0,0,.55);display:flex;align-items:center;justify-content:center}
.hero-arrow.prev{left:0}.hero-arrow.next{right:0}

.services{height:275px;background:var(--white);padding-top:18px}
.service-grid{width:656px;margin:0 auto;display:flex;justify-content:space-between}
.service{width:146px;text-align:center}
.service h2{font-family:"Roboto Condensed",Arial,sans-serif;font-size:12px;font-weight:700;line-height:1.15;height:30px;color:#222}
.service-photo{height:118px;margin:6px 0 10px;border:1px solid var(--line)}
.service p{font-size:8.5px;line-height:1.4;color:var(--muted);text-align:left;height:36px}
.read-more{display:inline-block;margin-top:6px;font-size:9px;font-weight:700;color:var(--brand)}

.about{height:115px;background:var(--band);color:var(--white);text-align:center;padding-top:20px}
.about h2{font-family:"Roboto Condensed",Arial,sans-serif;font-size:14px;font-weight:700;letter-spacing:.4px}
.about p{width:620px;margin:14px auto 0;font-size:9px;line-height:1.5;color:#ccc}

.blog{height:317px;background:var(--page);padding-top:40px}
.section-title{text-align:center;font-family:"Roboto Condensed",Arial,sans-serif;font-size:14px;font-weight:400;color:#555}
.section-title::after{content:"";display:block;width:40px;height:2px;background:var(--brand);margin:6px auto 0}
.post-grid{width:660px;margin:22px auto 0;display:flex;justify-content:space-between}
.post{width:206px;background:var(--white);border:1px solid var(--line);box-shadow:0 2px 4px rgba(0,0,0,.12)}
.post-photo{height:96px;position:relative;background:linear-gradient(#c9d4de,#8fa3b6)}
.post-date{position:absolute;left:0;bottom:0;background:var(--brand);color:var(--white);font-size:8px;padding:2px 6px}
.post-body{padding:7px 8px 10px}
.post h3{font-size:10.5px;font-weight:700;color:var(--brand)}
.post p{font-size:8.5px;line-height:1.35;color:var(--muted);margin-top:4px}

.site-footer{height:88px;background:var(--footer);color:#dce6f5;font-size:8.5px;padding:16px 112px 0}
.footer-nav{display:flex;gap:12px;color:var(--white);font-weight:600}
.footer-line{margin-top:9px;display:flex;justify-content:space-between}
</style>
</head>
<body>
<header class="site-header">
  <div class="brand"><span class="brand-mark"></span><span class="brand-name">Norbridge Solutions Group</span></div>
  <div class="call">
    <svg viewBox="0 0 24 24"><path fill="#1a5fb4" d="M6.6 10.8a15 15 0 0 0 6.6 6.6l2.2-2.2a1 1 0 0 1 1-.25 11.4 11.4 0 0 0 3.6.57 1 1 0 0 1 1 1V20a1 1 0 0 1-1 1A17 17 0 0 1 3 4a1 1 0 0 1 1-1h3.5a1 1 0 0 1 1 1c0 1.25.2 2.45.57 3.57a1 1 0 0 1-.25 1z"/></svg>
    <div class="call-text">Call Us Today<strong>07 5550 1234</strong></div>
  </div>
  <nav class="main-nav">
    <a href="#" class="is-active">Home</a><a href="#">About Us</a><a href="#">Services</a><a href="#">Blog Posts</a><a href="#">Contact Us</a>
  </nav>
</header>

<section class="hero">
  <div class="hero-photo" role="img" aria-label="Hand touching a glowing network of connected nodes on a dark blue background"></div>
  <div class="hero-copy">
    <h1>Managed IT Service Solutions</h1>
    <p>Reliable and Responsive 24/7</p>
  </div>
  <a href="#" class="hero-arrow prev"><svg width="8" height="12" viewBox="0 0 8 12"><path d="M6 1 1 6l5 5" fill="none" stroke="#fff" stroke-width="2"/></svg></a>
  <a href="#" class="hero-arrow next"><svg width="8" height="12" viewBox="0 0 8 12"><path d="m2 1 5 5-5 5" fill="none" stroke="#fff" stroke-width="2"/></svg></a>
</section>

<section class="services">
  <div class="service-grid">
    <article class="service">
      <h2>TECHNOLOGY<br>CONSULTING</h2>
      <div class="service-photo" role="img" aria-label="Business people shaking hands in an office" style="background:linear-gradient(#dfe7ef,#8fa6bd)"></div>
      <p>Practical advice that aligns your technology with business goals and growth.</p>
      <a href="#" class="read-more">Read More</a>
    </article>
    <article class="service">
      <h2>MANAGED IT<br>SERVICES</h2>
      <div class="service-photo" role="img" aria-label="Technician working in a server room" style="background:linear-gradient(#b9c3cc,#4d5d6c)"></div>
      <p>Proactive monitoring and support that keeps your systems running smoothly.</p>
      <a href="#" class="read-more">Read More</a>
    </article>
    <article class="service">
      <h2>CLOUD SERVICES<br>&amp; HOSTING</h2>
      <div class="service-photo" role="img" aria-label="Hand holding a glowing cloud symbol" style="background:linear-gradient(#eef3f8,#a8c0d8)"></div>
      <p>Secure, scalable hosting that moves your workloads to the cloud with ease.</p>
      <a href="#" class="read-more">Read More</a>
    </article>
    <article class="service">
      <h2>SOFTWARE<br>DEVELOPMENT</h2>
      <div class="service-photo" role="img" aria-label="Developer typing code on a laptop" style="background:linear-gradient(#d7dbe0,#7b8794)"></div>
      <p>Custom applications built around the way your team actually works.</p>
      <a href="#" class="read-more">Read More</a>
    </article>
  </div>
</section>

<section class="about">
  <h2>ABOUT NORBRIDGE SOLUTIONS GROUP</h2>
  <p>Norbridge Solutions Group offers technology consulting, managed IT services and a research cloud platform for businesses of every size, with offices in two cities. Our aspiration is delivering the most reliable, responsive and practical support to every client we work with.</p>
</section>

<section class="blog">
  <h2 class="section-title">Blog Posts</h2>
  <div class="post-grid">
    <article class="post">
      <div class="post-photo" role="img" aria-label="Portrait of a smiling businessman in a blue shirt"><span class="post-date">June 18, 2014</span></div>
      <div class="post-body">
        <h3>Consumer Partnership</h3>
        <p>How shared goals between provider and client create lasting value for both sides.</p>
        <a href="#" class="read-more">Read More</a>
      </div>
    </article>
    <article class="post">
      <div class="post-photo" role="img" aria-label="Portrait of a smiling businessman in a blue shirt"><span class="post-date">June 25, 2014</span></div>
      <div class="post-body">
        <h3>Cloud Data Transfer</h3>
        <p>Simple steps for moving large data sets quickly, safely and at a sensible cost.</p>
        <a href="#" class="read-more">Read More</a>
      </div>
    </article>
    <article class="post">
      <div class="post-photo" role="img" aria-label="Portrait of a smiling businessman in a blue shirt"><span class="post-date">July 31, 2014</span></div>
      <div class="post-body">
        <h3>Moving Data into the Cloud</h3>
        <p>A checklist for planning your migration and avoiding common pitfalls along the way.</p>
        <a href="#" class="read-more">Read More</a>
      </div>
    </article>
  </div>
</section>

<footer class="site-footer">
  <nav class="footer-nav"><a href="#">Home</a><a href="#">About Us</a><a href="#">Services</a><a href="#">Blog Posts</a><a href="#">Contact Us</a></nav>
  <div class="footer-line"><span>Level 2, 10 Harbour Lane, Springfield, QLD 4300</span></div>
  <div class="footer-line"><span>07 5550 1234 &nbsp;|&nbsp; hello@norbridge.example</span><span>Copyright © 2014 Norbridge Solutions Group. All Rights Reserved.</span></div>
</footer>
</body>
</html>
```